PowerPoint Design Project

Design Brief
Corvanta is updating its stationary templates to reflect the company’s position as market leader in smart-location based solutions.
Using the existing Corvanta logo and corporate colours, create an engaging and visually appealing PowerPoint presentation template identity that works when printed on A4 and US Letter sized paper.
The successful designs will complement the current look and feel of the Corvanta website (www.corvanta-example.net) and communicate that Corvanta is a dynamic and modern technology company that is at the cutting edge of innovation.
Corvanta Brand
Corvanta stands for Precision Location Technology. The brand represents both a unique, highly innovative platform product and a mature consulting and support organisation dedicated to delivering solutions to blue-chip customer problems. The orange colour implies creativity while blue evokes trust and a rational approach. “Cor” is Latin and means “where”, so the brand directly addresses the focus of the company: location. “Sense” can mean that we have sensing technology to support our precision location aware applications and solutions, but also that we make sensible use of location data to improve customer processes.
Corvanta Corporate Profile
Corvanta is a market leader of location-based Smart Factory Solutions which enables companies to optimise their business processes. By keeping track of key assets, Corvanta solutions bring clarity to complex operations in industries while also improving quality and reliability. Corvanta uses a unique combination of advancefd industry knowledge and an experienced team to deliver effective and superior solutions that offer unprecedented visibility, control and accuracy, delivering time and cost savings. Corvanta solutions are easy to implement and flexible to a particular business’s needs, no matter which area of the globe they operate in.
Corvanta offers two location-oriented products; RTLS (Real-time Location Solutions) and Geospatial Systems and operates in a number of industries ranging from manufacturing and utilities to telecommunications and is used by a number of blue chip customers across the world, such as KLT, Skyvane, Dromtrack, Pellow Power, RIM and Nordfeld Fernmelde.
Corvanta Corporate Colours
Orange:
Pantone 021C
R: 237 / G: 110 / B: 0
C: 0 / M: 53 / Y: 100 / K: 0
Hex #ED6E00
Dark Blue:
Pantone 662C
R: 15 / G: 31 / B: 122
C: 100 / M: 71 / Y: 0 / K:0
Hex #0F1F7A
Light Blue:
Pantone 300C
R: 0 / G: 110 / B: 199
C: 100 / M: 44 / Y: 0 / K:0
Hex #006EC7
Corvanta Corporate Fonts
The preferred font is Tahoma for Title, Topics and Print. In certain situations, Arial is an acceptable alternative.
Target Market(s)
Manufacturing industry, Automotive and Aerospace
Industry/Entity Type
Telecommunications
Look and feel
Each slider illustrates characteristics of the customer's brand and the style your logo design should communicate.

```html
<!DOCTYPE html>
<html lang="en">
<head>
<meta charset="utf-8">
<title>Corvanta presentation template</title>
<link rel="stylesheet" href="https://fonts.googleapis.com/css2?family=Noto+Sans:wght@400;700&display=swap">
<style>
  :root {
    --orange: #ED6E00;
    --dark-blue: #0F1F7A;
    --light-blue: #006EC7;
    --header-deep: #0b3470;
    --header-mid: #1560ad;
    --text: #333333;
    --muted: #666666;
    --row-a: #f8d5c6;
    --row-b: #fce9e1;
    --wash: #fbf1ea;
  }
  * { box-sizing: border-box; margin: 0; padding: 0; }
  html, body { width: 1200px; height: 329px; overflow: hidden; background: #ffffff; }
  body { position: relative; font-family: "Noto Sans", Tahoma, sans-serif; color: var(--text); }

  .slide {
    position: absolute; top: 50px; width: 361px; height: 247px;
    background: #ffffff; box-shadow: 1px 2px 4px rgba(0,0,0,.35); overflow: hidden;
  }
  .slide--chart { left: 33px; }
  .slide--mixed { left: 428px; }
  .slide--table { left: 823px; }

  .slide__header {
    position: absolute; left: 0; top: 0; width: 100%; height: 38px;
    background: linear-gradient(90deg, var(--header-deep) 0%, var(--header-mid) 45%, var(--header-deep) 75%);
    border-bottom: 3px solid var(--orange);
  }
  .slide__title {
    position: absolute; left: 11px; top: 12px; color: #fff; font-size: 13px; letter-spacing: -.1px;
  }
  .brand {
    position: absolute; right: 4px; top: 2px; width: 114px; height: 34px; background: #fff;
    display: flex; align-items: center; justify-content: center; gap: 5px;
  }
  .brand__mark { width: 11px; height: 11px; border-radius: 50%; background: var(--orange); }
  .brand__name { font-size: 13px; font-weight: 700; color: var(--dark-blue); }

  .slide__wash {
    position: absolute; left: 0; top: 41px; width: 100%; height: 200px;
    background: radial-gradient(ellipse at 50% 45%, var(--wash) 0%, #ffffff 70%);
  }
  .slide__footer { position: absolute; left: 0; bottom: 0; width: 100%; height: 6px; background: var(--orange); }

  .slide__body { position: absolute; left: 0; top: 0; }
  .chart-text { font-family: "Noto Sans", Tahoma, sans-serif; }

  .bullets {
    position: absolute; left: 175px; top: 47px; width: 178px; height: 190px;
    border: 1px dashed #f0b88a; padding: 4px 8px 0 7px; list-style: none;
  }
  .bullets li {
    position: relative; padding-left: 13px; font-size: 6.2px; line-height: 10px; color: var(--text); margin-bottom: 5px;
  }
  .bullets li::before { content: "\2013"; position: absolute; left: 0; color: var(--orange); }

  .data-table-title {
    position: absolute; left: 0; top: 85px; width: 100%; text-align: center; color: var(--orange); font-size: 10px;
  }
  .data-table {
    position: absolute; left: 47px; top: 105px; width: 218px; border-collapse: collapse; font-size: 7.5px;
  }
  .data-table th { background: var(--orange); color: #fff; font-weight: 400; height: 12px; border: 1px solid #fff; }
  .data-table td { text-align: center; height: 12px; border: 1px solid #fff; }
  .data-table tbody tr:nth-child(odd) td { background: var(--row-a); }
  .data-table tbody tr:nth-child(even) td { background: var(--row-b); }
</style>
</head>
<body>

<section class="slide slide--chart">
  <div class="slide__wash" role="img" aria-label="Faint world map background"></div>
  <header class="slide__header">
    <h1 class="slide__title">Chart slide 1</h1>
    <div class="brand"><span class="brand__mark"></span><span class="brand__name">Corvanta</span></div>
  </header>
  <svg class="slide__body chart-text" width="361" height="247" viewBox="0 0 361 247">
    <text x="164" y="66" text-anchor="middle" fill="#ED6E00" font-size="10">Chart title</text>
    <line x1="55" y1="188" x2="270" y2="188" stroke="#bbb" stroke-width=".6"/>
    <g font-size="6.5" fill="#333" text-anchor="middle">
      <rect x="70" y="106" width="10" height="82" fill="#ED6E00"/><text x="75" y="103">4.3</text>
      <rect x="81" y="142" width="10" height="46" fill="#006EC7"/><text x="86" y="139">2.4</text>
      <rect x="92" y="150" width="10" height="38" fill="#0F1F7A"/><text x="97" y="147">2</text>
      <rect x="123" y="140" width="10" height="48" fill="#ED6E00"/><text x="128" y="137">2.5</text>
      <rect x="134" y="104" width="10" height="84" fill="#006EC7"/><text x="139" y="101">4.4</text>
      <rect x="145" y="150" width="10" height="38" fill="#0F1F7A"/><text x="150" y="147">2</text>
      <rect x="174" y="121" width="10" height="67" fill="#ED6E00"/><text x="179" y="118">3.5</text>
      <rect x="185" y="154" width="10" height="34" fill="#006EC7"/><text x="190" y="151">1.8</text>
      <rect x="196" y="131" width="10" height="57" fill="#0F1F7A"/><text x="201" y="128">3</text>
      <rect x="226" y="102" width="10" height="86" fill="#ED6E00"/><text x="231" y="99">4.5</text>
      <rect x="237" y="135" width="10" height="53" fill="#006EC7"/><text x="242" y="132">2.8</text>
      <rect x="248" y="93" width="10" height="95" fill="#0F1F7A"/><text x="253" y="90">5</text>
      <text x="87" y="198">Category 1</text>
      <text x="140" y="198">Category 2</text>
      <text x="191" y="198">Category 3</text>
      <text x="243" y="198">Category 4</text>
    </g>
    <g font-size="6" fill="#333">
      <rect x="118" y="205" width="5" height="5" fill="#ED6E00"/><text x="125" y="210">Series 1</text>
      <rect x="151" y="205" width="5" height="5" fill="#006EC7"/><text x="158" y="210">Series 2</text>
      <rect x="184" y="205" width="5" height="5" fill="#0F1F7A"/><text x="191" y="210">Series 3</text>
    </g>
  </svg>
  <div class="slide__footer"></div>
</section>

<section class="slide slide--mixed">
  <div class="slide__wash" role="img" aria-label="Faint world map background"></div>
  <header class="slide__header">
    <h1 class="slide__title">Several charts + text slide</h1>
    <div class="brand"><span class="brand__mark"></span><span class="brand__name">Corvanta</span></div>
  </header>
  <svg class="slide__body chart-text" width="361" height="247" viewBox="0 0 361 247">
    <rect x="12" y="47" width="157" height="91" fill="#fff" stroke="#f0b88a" stroke-dasharray="2 1.5" stroke-width=".8"/>
    <rect x="12" y="144" width="157" height="93" fill="#fff" stroke="#f0b88a" stroke-dasharray="2 1.5" stroke-width=".8"/>
    <g font-size="5" fill="#333">
      <line x1="34" y1="55" x2="34" y2="125" stroke="#999" stroke-width=".5"/>
      <line x1="34" y1="125" x2="135" y2="125" stroke="#999" stroke-width=".5"/>
      <text x="28" y="127">0</text><text x="28" y="104">2</text><text x="28" y="80">4</text><text x="28" y="57">6</text>
      <text x="41" y="133">2010</text><text x="66" y="133">2011</text><text x="91" y="133">2012</text><text x="116" y="133">2013</text>
      <polyline points="48,75 73,96 98,84 123,72" fill="none" stroke="#ED6E00" stroke-width="1"/>
      <polyline points="48,97 73,74 98,104 123,92" fill="none" stroke="#006EC7" stroke-width="1"/>
      <polyline points="48,102 73,102 98,90 123,66" fill="none" stroke="#0F1F7A" stroke-width="1"/>
      <g fill="#ED6E00"><circle cx="48" cy="75" r="1.5"/><circle cx="73" cy="96" r="1.5"/><circle cx="98" cy="84" r="1.5"/><circle cx="123" cy="72" r="1.5"/></g>
      <g fill="#006EC7"><rect x="46.5" y="95.5" width="3" height="3"/><rect x="71.5" y="72.5" width="3" height="3"/><rect x="96.5" y="102.5" width="3" height="3"/><rect x="121.5" y="90.5" width="3" height="3"/></g>
      <line x1="141" y1="84" x2="149" y2="84" stroke="#ED6E00"/><text x="151" y="86">A</text>
      <line x1="141" y1="93" x2="149" y2="93" stroke="#006EC7"/><text x="151" y="95">B</text>
      <line x1="141" y1="102" x2="149" y2="102" stroke="#0F1F7A"/><text x="151" y="104">C</text>

      <line x1="34" y1="153" x2="34" y2="222" stroke="#999" stroke-width=".5"/>
      <text x="17" y="161">2013</text><text x="17" y="179">2012</text><text x="17" y="197">2011</text><text x="17" y="215">2010</text>
      <rect x="34" y="154" width="78" height="3" fill="#0F1F7A"/><rect x="34" y="157" width="43" height="3" fill="#006EC7"/><rect x="34" y="160" width="70" height="3" fill="#ED6E00"/>
      <rect x="34" y="172" width="47" height="3" fill="#0F1F7A"/><rect x="34" y="175" width="28" height="3" fill="#006EC7"/><rect x="34" y="178" width="54" height="3" fill="#ED6E00"/>
      <rect x="34" y="190" width="31" height="3" fill="#0F1F7A"/><rect x="34" y="193" width="68" height="3" fill="#006EC7"/><rect x="34" y="196" width="39" height="3" fill="#ED6E00"/>
      <rect x="34" y="208" width="31" height="3" fill="#0F1F7A"/><rect x="34" y="211" width="37" height="3" fill="#006EC7"/><rect x="34" y="214" width="67" height="3" fill="#ED6E00"/>
      <text x="33" y="231">0</text><text x="64" y="231">2</text><text x="95" y="231">4</text><text x="126" y="231">6</text>
      <rect x="138" y="183" width="3" height="3" fill="#0F1F7A"/><text x="144" y="186">C</text>
      <rect x="138" y="192" width="3" height="3" fill="#006EC7"/><text x="144" y="195">B</text>
      <rect x="138" y="201" width="3" height="3" fill="#ED6E00"/><text x="144" y="204">A</text>
    </g>
  </svg>
  <ul class="bullets">
    <li>Lorem ipsum dolor sit amet, consectetur adipiscing elit. Proin in velit facilisis libero consectetur adipiscing.</li>
    <li>Aenean congue euismod erat, eu adipiscing dui gravida in.</li>
    <li>Donec vehicula tellus sit amet est aliquam ac pretium lacus aliquam.</li>
    <li>Suspendisse potenti. Integer est nunc, dignissim ac sagittis sit amet, pretium sit amet libero.</li>
    <li>Cras id nibh et ipsum ultrices pretium. Curabitur id leo tellus, a convallis justo. In turpis magna, aliquam ut consequat et, tempor ultrices mauris.</li>
  </ul>
  <div class="slide__footer"></div>
</section>

<section class="slide slide--table">
  <div class="slide__wash" role="img" aria-label="Faint world map background"></div>
  <header class="slide__header">
    <h1 class="slide__title">Table slide</h1>
    <div class="brand"><span class="brand__mark"></span><span class="brand__name">Corvanta</span></div>
  </header>
  <h2 class="data-table-title">Table Title</h2>
  <table class="data-table">
    <thead><tr><th>Category A</th><th>Category B</th><th>Category C</th><th>Category D</th></tr></thead>
    <tbody>
      <tr><td>111.222</td><td>111.333</td><td>111.444</td><td>111.999</td></tr>
      <tr><td>222.333</td><td>222.444</td><td>222.333</td><td>222.333</td></tr>
      <tr><td>333.444</td><td>333.555</td><td>333.888</td><td>333.999</td></tr>
      <tr><td>444.555</td><td>444.222</td><td>444.777</td><td>444.555</td></tr>
      <tr><td>555.222</td><td>555.777</td><td>555.888</td><td>555.222</td></tr>
    </tbody>
  </table>
  <div class="slide__footer"></div>
</section>

</body>
</html>
```